Coffeeshop menu for filter tip

We want to have a cannabis (coffeeshop) menu in the size 25mm wide x 60mm wide. Some examples attached.

it must have the following text:
Menu

WEED p/g
Vortigan €16
Tangerosa €14
Dusk Rover €14
Mangolina €16
Ultra Fern €14
Amber Hermit €14

HASH p/g
Nepali Bronze €12
Velvet Ember€11
Cedar Pine €14
Red Fable €10

Target Market(s)

tourist in Amsterdam

Requirements
Nice to have
• cannabis sign leaf
• No Cigarettes allowed symbol

```html
<!DOCTYPE html>
<html lang="en">
<head>
<meta charset="utf-8">
<title>Grachten Cafe Menu</title>
<link rel="stylesheet" href="https://fonts.googleapis.com/css2?family=Griffy&family=Gochi+Hand&family=Bangers&display=swap">
<style>
  :root {
    --yellow-deep: #f5ea12;
    --yellow-light: #fffbd6;
    --title-green: #1f9c1f;
    --title-edge: #0b5a0b;
    --item-green: #1e8a1e;
    --price-green: #2a9a2a;
    --heading-red: #e0261c;
    --heading-edge: #8a1008;
    --leaf-green: #2e8b2e;
    --leaf-dark: #1a5e1a;
    --footer-ink: #5a1a10;
    --sign-red: #d8201a;
  }
  html, body {
    margin: 0;
    padding: 0;
    overflow: hidden;
  }
  .menu {
    position: relative;
    width: 1200px;
    height: 2880px;
    overflow: hidden;
    background: radial-gradient(ellipse 900px 1300px at 50% 62%, var(--yellow-light) 0%, #fdf67a 55%, var(--yellow-deep) 100%);
  }
  .title {
    position: absolute;
    left: 0;
    width: 1200px;
    margin: 0;
    text-align: center;
    font-family: "Griffy", cursive;
    font-weight: 400;
    color: var(--title-green);
    -webkit-text-stroke: 4px var(--title-edge);
    line-height: 1;
  }
  .title-top { top: 70px; font-size: 200px; }
  .title-bottom { top: 320px; font-size: 200px; }
  .leaf-art {
    position: absolute;
    border-radius: 50% 50% 45% 45%;
    background: radial-gradient(ellipse at 50% 45%, var(--leaf-green) 0%, var(--leaf-dark) 70%, rgba(26, 94, 26, 0) 100%);
  }
  .leaf-left { left: 80px; top: 520px; width: 400px; height: 320px; }
  .leaf-right { left: 640px; top: 540px; width: 520px; height: 460px; }
  .section-head {
    position: absolute;
    font-family: "Bangers", cursive;
    font-size: 96px;
    color: var(--heading-red);
    -webkit-text-stroke: 2px var(--heading-edge);
    line-height: 1;
    letter-spacing: 2px;
  }
  .unit {
    position: absolute;
    left: 760px;
    font-family: "Gochi Hand", cursive;
    font-size: 96px;
    color: var(--heading-red);
    line-height: 1;
  }
  .item {
    position: absolute;
    left: 0;
    width: 1200px;
    height: 100px;
  }
  .item-name {
    position: absolute;
    left: 320px;
    transform: translateX(-50%);
    white-space: nowrap;
    font-family: "Gochi Hand", cursive;
    font-size: 68px;
    color: var(--item-green);
    line-height: 100px;
  }
  .item-price {
    position: absolute;
    left: 730px;
    font-family: "Gochi Hand", cursive;
    font-size: 100px;
    color: var(--price-green);
    line-height: 100px;
    letter-spacing: 6px;
  }
  .notice {
    position: absolute;
    left: 310px;
    top: 2748px;
    display: flex;
    align-items: center;
    gap: 28px;
  }
  .notice-icon { width: 84px; height: 84px; }
  .notice-text {
    font-family: "Gochi Hand", cursive;
    font-size: 44px;
    color: var(--footer-ink);
  }
</style>
</head>
<body>
<main class="menu">
  <h1 class="title title-top">Grachten</h1>
  <h1 class="title title-bottom">Cafe</h1>

  <div class="leaf-art leaf-left" role="img" aria-label="Green cannabis leaf illustration"></div>
  <div class="leaf-art leaf-right" role="img" aria-label="Large green cannabis leaf illustration"></div>

  <section class="price-list weed">
    <div class="section-head" style="left:170px; top:1052px;">WEED</div>
    <div class="unit" style="top:1050px;">p/g</div>
    <div class="item" style="top:1214px;"><span class="item-name">Vortigan</span><span class="item-price">€ 16</span></div>
    <div class="item" style="top:1338px;"><span class="item-name">Tangerosa</span><span class="item-price">€ 14</span></div>
    <div class="item" style="top:1462px;"><span class="item-name">Dusk Rover</span><span class="item-price">€ 14</span></div>
    <div class="item" style="top:1586px;"><span class="item-name">Mangolina</span><span class="item-price">€ 16</span></div>
    <div class="item" style="top:1702px;"><span class="item-name">Ultra Fern</span><span class="item-price">€ 14</span></div>
    <div class="item" style="top:1822px;"><span class="item-name">Amber Hermit</span><span class="item-price">€ 14</span></div>
  </section>

  <section class="price-list hash">
    <div class="section-head" style="left:170px; top:2060px;">HASH</div>
    <div class="unit" style="top:2058px;">p/g</div>
    <div class="item" style="top:2198px;"><span class="item-name">Nepali Bronze</span><span class="item-price">€ 12</span></div>
    <div class="item" style="top:2334px;"><span class="item-name">Velvet Ember</span><span class="item-price">€ 11</span></div>
    <div class="item" style="top:2486px;"><span class="item-name">Cedar Pine</span><span class="item-price">€ 14</span></div>
    <div class="item" style="top:2622px;"><span class="item-name">Red Fable</span><span class="item-price">€ 10</span></div>
  </section>

  <div class="notice">
    <svg class="notice-icon" viewBox="0 0 84 84" aria-hidden="true">
      <circle cx="42" cy="42" r="38" fill="#ffffff" stroke="var(--sign-red)" stroke-width="7"/>
      <rect x="16" y="38" width="40" height="9" fill="#444"/>
      <rect x="56" y="38" width="10" height="9" fill="#c77a2a"/>
      <path d="M60 34 q4 -8 0 -14" fill="none" stroke="#888" stroke-width="3"/>
      <line x1="16" y1="16" x2="68" y2="68" stroke="var(--sign-red)" stroke-width="7"/>
    </svg>
    <span class="notice-text">Cigarettes not allowed</span>
  </div>
</main>
</body>
</html>
```